Stationary for Tovin Consulting

Hi

I am after stationary designs for my company - Tovin Consulting. I have a logo - recently designed by ArtHarbor. Tovin ( nivot spelt backwards ) is a sales consultancy - including sales training, sales coaching and business management.

I have attached some of the artwork I already have, as well as a few ideas
1. Use supplied logo's
2. back of business card to use the logo with the dark background and white text
3. details to be included on card are
Logo
Delia Marquand
p: +61409827316
e: delia@tovinconsulting.com.au
w: www.tovinconsulting.com.au
PO Box 412, Kelby Heights, Victoria, 3187

4. I am after designs for business cards, A4 letterhead and A5 letterhead

Thanks in Advance

Delia

Industry/Entity Type

It Company

```html
<!DOCTYPE html>
<html lang="en">
<head>
<meta charset="utf-8">
<title>Tovin Consulting — Stationery</title>
<link href="https://fonts.googleapis.com/css2?family=Arimo:wght@400;700&display=swap" rel="stylesheet">
<style>
  :root {
    --slate: #2f4652;
    --ember: #e0502a;
    --paper: #ffffff;
    --backdrop: #6b6b6b;
    --ink: #1f1f1f;
  }
  * { margin: 0; padding: 0; box-sizing: border-box; }
  html, body { width: 1200px; height: 1000px; overflow: hidden; }
  body {
    background: var(--backdrop);
    font-family: "Arimo", Arial, sans-serif;
    position: relative;
  }
  .sheet { position: absolute; background: var(--paper); overflow: hidden; }

  /* wordmark: invented name in one colour, one weight */
  .wordmark {
    position: absolute;
    font-weight: 700;
    color: var(--slate);
    line-height: 1;
    text-transform: lowercase;
  }
  .wordmark .name { display: block; }
  .wordmark .sub { display: block; text-transform: uppercase; letter-spacing: 0.3em; }
  .wordmark.on-dark { color: var(--paper); }

  /* business card front */
  .card-front { left: 115px; top: 34px; width: 308px; height: 190px; }
  .card-front .band-slate { position: absolute; left: 0; top: 0; width: 18px; height: 100%; background: var(--slate); }
  .card-front .band-ember { position: absolute; left: 18px; top: 0; width: 6px; height: 100%; background: var(--ember); }
  .card-front .wordmark { right: 23px; top: 22px; text-align: left; }
  .card-front .wordmark .name { font-size: 30px; }
  .card-front .wordmark .sub { font-size: 8px; margin-top: 2px; }
  .card-front .holder { position: absolute; left: 40px; top: 80px; }
  .holder-name { font-size: 13px; font-weight: 700; color: var(--slate); }
  .holder-role { font-size: 6.5px; color: #555; margin-top: 3px; }
  .card-front .contact { position: absolute; left: 40px; top: 117px; font-size: 7px; color: var(--ink); line-height: 15px; }

  /* card back and alternate */
  .card-dark { left: 444px; top: 34px; width: 308px; height: 190px; background: var(--slate); }
  .card-light { left: 777px; top: 34px; width: 308px; height: 190px; }
  .card-dark .wordmark, .card-light .wordmark { left: 50%; top: 50%; transform: translate(-50%, -50%); text-align: center; }
  .card-dark .wordmark .name, .card-light .wordmark .name { font-size: 46px; }
  .card-dark .wordmark .sub, .card-light .wordmark .sub { font-size: 13px; margin-top: 6px; }

  /* letterhead */
  .letterhead { left: 56px; top: 259px; width: 506px; height: 715px; }
  .letterhead .wordmark { right: 41px; top: 26px; }
  .letterhead .wordmark .name { font-size: 36px; }
  .letterhead .wordmark .sub { font-size: 10px; margin-top: 3px; }

  .footer-band { position: absolute; display: flex; }
  .footer-band .slate { background: var(--slate); }
  .footer-band .ember { background: var(--ember); }
  .footer-text { position: absolute; font-size: 6px; font-weight: 700; color: var(--ink); line-height: 8.5px; }

  .letterhead .footer-band { left: 0; top: 670px; height: 45px; }
  .letterhead .footer-band .slate { width: 24px; }
  .letterhead .footer-band .ember { width: 10px; }
  .letterhead .footer-text { left: 44px; top: 673px; }

  /* envelope front */
  .envelope-front { left: 603px; top: 325px; width: 565px; height: 269px; }
  .envelope-front .wordmark { left: 39px; top: 28px; }
  .envelope-front .wordmark .name { font-size: 33px; }
  .envelope-front .wordmark .sub { font-size: 9px; margin-top: 3px; }
  .envelope-front .footer-band { left: 0; top: 91px; height: 29px; }
  .envelope-front .footer-band .slate { width: 24px; }
  .envelope-front .footer-band .ember { width: 10px; }
  .envelope-front .footer-text { left: 44px; top: 91px; }

  /* envelope back */
  .envelope-back { left: 603px; top: 629px; width: 560px; height: 268px; }
  .envelope-back .flap { position: absolute; left: 0; top: 0; }
  .envelope-back .wordmark { left: 50%; top: 24px; transform: translateX(-50%); }
  .envelope-back .wordmark .name { font-size: 32px; }
</style>
</head>
<body>

  <section class="sheet card-front" aria-label="Business card front">
    <div class="band-slate"></div>
    <div class="band-ember"></div>
    <div class="wordmark"><span class="name">tovin</span><span class="sub">Consulting</span></div>
    <div class="holder">
      <p class="holder-name">Delia Marquand</p>
      <p class="holder-role">Owner / Founder</p>
    </div>
    <div class="contact">
      <p>M&nbsp; +61409827316</p>
      <p>E&nbsp; delia@tovinconsulting.com.au</p>
      <p>W&nbsp; www.tovinconsulting.com.au</p>
      <p>PO Box 412, Kelby Heights, Victoria, 3187</p>
    </div>
  </section>

  <section class="sheet card-dark" aria-label="Business card back">
    <div class="wordmark on-dark"><span class="name">tovin</span><span class="sub">Consulting</span></div>
  </section>

  <section class="sheet card-light" aria-label="Business card alternate back">
    <div class="wordmark"><span class="name">tovin</span><span class="sub">Consulting</span></div>
  </section>

  <section class="sheet letterhead" aria-label="A4 letterhead">
    <div class="wordmark"><span class="name">tovin</span><span class="sub">Consulting</span></div>
    <div class="footer-band"><div class="slate"></div><div class="ember"></div></div>
    <div class="footer-text">
      <p>e-mail: delia@tovinconsulting.com.au</p>
      <p>web: www.tovinconsulting.com.au</p>
      <p>PO Box 412, Kelby Heights, Victoria, 3187</p>
    </div>
  </section>

  <section class="sheet envelope-front" aria-label="Envelope front">
    <div class="wordmark"><span class="name">tovin</span><span class="sub">Consulting</span></div>
    <div class="footer-band"><div class="slate"></div><div class="ember"></div></div>
    <div class="footer-text">
      <p>e-mail: delia@tovinconsulting.com.au</p>
      <p>web: www.tovinconsulting.com.au</p>
      <p>PO Box 412, Kelby Heights, Victoria, 3187</p>
    </div>
  </section>

  <section class="sheet envelope-back" aria-label="Envelope back">
    <svg class="flap" width="560" height="80" viewBox="0 0 560 80">
      <path d="M0.5 0 C6 40 18 74 40 74 L520 74 C542 74 554 40 559.5 0" fill="none" stroke="#444" stroke-width="0.8"/>
    </svg>
    <div class="wordmark"><span class="name">tovin</span></div>
  </section>

</body>
</html>
```